Life Coach for Lawyers Business Card Design

Elegant, original, business card design for life coaching service for associate attorneys who work in big law and struggle with stress, overwhelm, and time management. Double sided design.

Target Market(s)

Women associate attorneys who work in big law and struggle with stress, overwhelm, and time management.

Industry/Entity Type

Life Coaching

Contact Information for Business Card

Marissa Pendrell
Life Coach
518.677.3941
calmbriefcounsel.net
marissa@calmbriefcounsel.net
@calmbriefcounsel (Instagram)

Font styles to use
Other font styles liked:
• Silver South font duo. See uploaded files.

Requirements
Must have
• Icons for phone, website, email, and Instagram instead of words. Specific colors used in my logo (171B2B, 421121, FFFFFF)
Nice to have
• Foil. Embossed. Feminine design.
Should not have
• Any colors other than those used in logo. See uploaded files.

```html
<!DOCTYPE html>
<html lang="en">
<head>
<meta charset="utf-8">
<title>Calm Brief Counsel – Business Card</title>
<link href="https://fonts.googleapis.com/css2?family=Josefin+Sans:wght@300;400;600&display=swap" rel="stylesheet">
<style>
  :root {
    --plum: #3a1e2b;
    --chevron: #5f4953;
    --muted: #8d7a83;
    --paper: #ffffff;
    --ink: #3a1e2b;
    --backdrop: #ece9ea;
  }
  * { margin: 0; padding: 0; box-sizing: border-box; }
  html, body { width: 1200px; height: 1200px; overflow: hidden; }
  body {
    background: var(--backdrop);
    font-family: "Josefin Sans", "Helvetica Neue", sans-serif;
    display: flex;
    flex-direction: column;
    align-items: center;
    justify-content: center;
    gap: 60px;
  }
  .card {
    position: relative;
    width: 900px;
    height: 514px;
    overflow: hidden;
    box-shadow: 0 10px 30px rgba(58, 30, 43, 0.18);
  }

  /* Back side */
  .card-back { background: var(--plum); color: var(--paper); }
  .card-back .chevrons { position: absolute; inset: 0; }
  .brand {
    position: absolute;
    left: 0; right: 0; top: 175px;
    text-align: center;
  }
  .brand-name {
    font-weight: 300;
    font-size: 58px;
    letter-spacing: 6px;
    text-transform: uppercase;
    line-height: 1.2;
  }
  .brand-url {
    margin-top: 58px;
    font-weight: 300;
    font-size: 17px;
    letter-spacing: 1px;
  }

  /* Front side */
  .card-front { background: var(--paper); }
  .front-band {
    position: absolute;
    left: 0; top: 0; width: 100%; height: 235px;
    background: var(--plum);
  }
  .front-notch { position: absolute; left: 418px; top: 234px; }
  .holder { position: absolute; left: 0; right: 0; top: 90px; text-align: center; }
  .holder-name { color: var(--paper); font-weight: 400; font-size: 44px; letter-spacing: 1px; }
  .holder-role { color: var(--muted); font-weight: 300; font-size: 22px; margin-top: 8px; letter-spacing: 1px; }
  .contact {
    position: absolute;
    top: 296px; left: 62px; right: 62px;
    display: grid;
    grid-template-columns: 1.1fr 1fr;
    row-gap: 50px;
    column-gap: 40px;
  }
  .contact-item {
    display: flex;
    align-items: center;
    gap: 16px;
    color: var(--ink);
    font-size: 16px;
    font-weight: 400;
    line-height: 1.35;
    white-space: nowrap;
  }
  .contact-item svg { flex: none; width: 26px; height: 26px; }
  .front-rule {
    position: absolute;
    left: 0; bottom: 22px; width: 100%; height: 5px;
    background: var(--plum);
  }
</style>
</head>
<body>

  <section class="card card-back" aria-label="Card back">
    <svg class="chevrons" viewBox="0 0 900 514" aria-hidden="true">
      <polygon fill="var(--chevron)" points="0,30 150,257 0,484 0,384 84,257 0,130"/>
      <polygon fill="var(--chevron)" points="900,30 750,257 900,484 900,384 816,257 900,130"/>
    </svg>
    <div class="brand">
      <div class="brand-name">Calm Brief<br>Counsel</div>
      <div class="brand-url">www.calmbriefcounsel.net</div>
    </div>
  </section>

  <section class="card card-front" aria-label="Card front">
    <div class="front-band"></div>
    <svg class="front-notch" width="64" height="22" viewBox="0 0 64 22" aria-hidden="true">
      <polygon fill="var(--chevron)" points="0,0 64,0 32,22"/>
    </svg>
    <div class="holder">
      <div class="holder-name">Marissa Pendrell</div>
      <div class="holder-role">Life Coach</div>
    </div>

    <div class="contact">
      <div class="contact-item contact-social">
        <svg viewBox="0 0 24 24" fill="none" stroke="var(--ink)" stroke-width="1.4" aria-hidden="true">
          <rect x="4" y="4" width="16" height="16"/>
        </svg>
        <span>@calmbriefcounsel</span>
      </div>
      <div class="contact-item contact-phone">
        <svg viewBox="0 0 24 24" fill="none" stroke="var(--ink)" stroke-width="1.4" aria-hidden="true">
          <path d="M6 3h3l1.5 4-2 1.5a11 11 0 0 0 6 6L16 12.5l4 1.5v3a2 2 0 0 1-2 2A15 15 0 0 1 4 5a2 2 0 0 1 2-2z"/>
        </svg>
        <span>518.677.3941</span>
      </div>
      <div class="contact-item contact-email">
        <svg viewBox="0 0 24 24" fill="none" stroke="var(--ink)" stroke-width="1.4" aria-hidden="true">
          <rect x="3" y="6" width="18" height="13" rx="1"/><path d="M3 7l9 7 9-7"/>
        </svg>
        <span>marissa@calmbriefcounsel.net</span>
      </div>
      <div class="contact-item contact-web">
        <svg viewBox="0 0 24 24" fill="none" stroke="var(--ink)" stroke-width="1.4" aria-hidden="true">
          <circle cx="12" cy="12" r="9"/><ellipse cx="12" cy="12" rx="4" ry="9"/><path d="M3 12h18M5 7h14M5 17h14"/>
        </svg>
        <span>www.calmbriefcounsel.net</span>
      </div>
    </div>
    <div class="front-rule"></div>
  </section>

</body>
</html>
```